Interfaith organization needs a poster advertising event for youth

We need a poster advertising our annual Lantern Gathering and Summit, where youth of all different religions come together for dialogue, friendship, fun, art, and musical performances. The poster should be have a front advertising the event, and the back should have more detailed descriptions of the event and submissions. It should be fun and eye catching!

Target Market(s)

Youth and Religious Organizations

Industry/Entity Type

Festival

Font styles to use
Serif

Requirements
Must have
• Pictures, poster-feel, contact information, etc. Logos of Bright Harbor Allies and Crossroads Young Leaders Circle of Maple Valley

```html
<!DOCTYPE html>
<html lang="en">
<head>
<meta charset="utf-8">
<title>Lantern Gathering and Summit Poster</title>
<link rel="stylesheet" href="https://fonts.googleapis.com/css2?family=League+Gothic&family=Tinos:wght@400;700&display=swap">
<style>
:root{
  --navy:#12213a;
  --ink:#1b1d2a;
  --brand:#2a62a8;
  --gold:#b89a5a;
  --sky-light:#eef6fd;
  --sky-mid:#c6dff3;
  --sky-deep:#8fbde3;
  --photo-warm:#6e4b3f;
  --photo-room:#8b8a8e;
}
*{margin:0;padding:0;box-sizing:border-box}
html,body{width:1200px;height:800px;overflow:hidden;background:#fff}
.poster{position:relative;width:1200px;height:800px;display:flex}
.panel{position:relative;width:600px;height:800px;overflow:hidden;
  background:radial-gradient(ellipse at 30% 20%,var(--sky-light) 0%,var(--sky-mid) 55%,var(--sky-deep) 100%)}
.panel-back{background:radial-gradient(ellipse at 50% 40%,#ffffff 0%,var(--sky-light) 45%,var(--sky-mid) 85%,var(--sky-deep) 100%)}
.photo{position:absolute;border-radius:2px}
.logo-council{position:absolute;left:92px;top:40px;display:flex;align-items:center;gap:10px;width:170px}
.logo-council .mark{width:34px;height:34px;border-radius:50%;background:var(--gold);flex:none}
.logo-council span{font-family:"Tinos",serif;font-weight:700;font-size:14px;line-height:1.2;color:var(--gold)}
.logo-partner{position:absolute;left:278px;top:34px;display:flex;align-items:center;gap:14px}
.logo-partner span{font-family:"Tinos",serif;font-size:40px;line-height:.95;color:var(--brand);width:130px}
.logo-partner .mark{width:72px;height:72px;border-radius:50%;border:3px solid var(--navy);flex:none}
.head{position:absolute;left:0;width:600px;text-align:center;font-family:"League Gothic",sans-serif;font-weight:400;color:var(--navy);text-transform:uppercase;line-height:1;white-space:nowrap}
.h1{top:231px;font-size:21px}
.h2{top:265px;font-size:28px}
.h3{top:299px;font-size:23px}
.theme{top:366px;font-size:48px}
.d1{top:446px;font-size:26px}
.d2{top:478px;font-size:26px}
.d3{top:510px;font-size:26px}
.body{font-family:"Tinos",serif;font-size:13.4px;line-height:16.6px;color:var(--ink);text-align:center;position:absolute}
.intro{left:28px;top:27px;width:548px}
.sect-title{display:block;text-decoration:underline}
.forum{left:38px;top:109px;width:284px}
.festival{left:26px;top:442px;width:552px}
.gallery{left:356px;top:572px;width:234px}
</style>
</head>
<body>
<div class="poster">
  <section class="panel panel-front">
    <div class="logo-council"><div class="mark"></div><span>Crossroads Young Leaders Circle of Maple Valley</span></div>
    <div class="logo-partner"><span>Bright Harbor Allies</span><div class="mark"></div></div>

    <div class="head h1">Crossroads Young Leaders Circle of Maple Valley's 13th Annual Lantern Gathering &amp; Summit</div>
    <div class="head h2">Teens expressing their faith through art, music, and dialogue</div>
    <div class="head h3">Interfaith Youth Forum</div>
    <div class="head theme">This year's theme "Is religion cool?"</div>
    <div class="head d1">Sunday March 19th, 2017 11:00AM-5:00PM</div>
    <div class="head d2">The Meridian Harmony Hall</div>
    <div class="head d3">4150 Willowbrook Ave, Maple Valley, CA 90417</div>

    <div class="photo" role="img" aria-label="Teen drummer performing on taiko drums" style="left:16px;top:565px;width:137px;height:206px;background:linear-gradient(160deg,#b9b4b0,var(--photo-warm))"></div>
    <div class="photo" role="img" aria-label="Table with candles and banners of many faith symbols" style="left:157px;top:574px;width:285px;height:192px;background:linear-gradient(180deg,#c9c6c4 0%,#8e2a36 60%,#6a1e28 100%)"></div>
    <div class="photo" role="img" aria-label="Dancer in red and yellow traditional dress" style="left:450px;top:565px;width:137px;height:207px;background:linear-gradient(180deg,#9aa8b8,#c9423a 70%,#e0b43a)"></div>
  </section>

  <section class="panel panel-back">
    <p class="body intro">All high school age faith groups are invited to come and join with 150 to 175 other high school students from various faith traditions to participate in the Crossroads Young Leaders Circle of Maple Valley's Annual Interfaith Youth Forum. More than ever, our county and world need young leaders who are willing to learn from each other and build stronger communities!</p>

    <p class="body forum"><span class="sect-title">LANTERN SUMMIT</span>The purpose of this Interfaith Youth Forum is to bring together young people from diverse ethnic, cultural, and religious backgrounds, and to engage them in dialogue. True dialogue is a conversation on a common subject between two or more persons of differing points of view and/or backgrounds. We feel that this commitment to dialogue will affect relationships in a constructive way in our places of worship and in our community. The forum itself involves having eight religiously diverse high school-age students, one adult, and youth leader around each table to discuss common questions. Our youth leaders act as facilitators, but it is stressed that it is the students we want to hear from. RSVP for our LANTERN SUMMIT by February 19th, 2017</p>

    <div class="photo" role="img" aria-label="Large room of students seated at round tables" style="left:333px;top:101px;width:232px;height:154px;background:linear-gradient(180deg,#d8d8d6 0%,var(--photo-room) 45%,#3e3a3c 100%)"></div>
    <div class="photo" role="img" aria-label="Student speaking to a seated group" style="left:333px;top:263px;width:232px;height:172px;background:linear-gradient(180deg,#b4b2ae 0%,#5c5452 60%,#2c2a2c 100%)"></div>

    <p class="body festival"><span class="sect-title">LANTERN GATHERING</span>The forum will be followed by the Lantern Gathering where families of the participants are welcomed to join. The Gathering will include musical performances of all types from diverse religious communities. The differing performing arts include but are not limited to singing, dancing, instrumental music, storytelling, etc.<br>To Participate in our Lantern Gathering (Music, Song, Dance), RSVP by February 25th, 2017</p>

    <div class="photo" role="img" aria-label="Students in discussion at tables in an art gallery room" style="left:30px;top:558px;width:320px;height:214px;background:linear-gradient(180deg,#a89c8c 0%,#6b5a66 55%,#3a3440 100%)"></div>

    <p class="body gallery"><span class="sect-title">ART GALLERY</span>This event will include and Art Gallery display of students' work, highlighting their expressions of faith, and artwork promoting learning, understanding, leadership, and service. Art includes any painting, illustration, sculpture, photography or other visual art. Art Work for our Art Galley must be submitted by: March 10th, 2017</p>
  </section>
</div>
</body>
</html>
```